New Stationary and Logo Design for Start Up Company

We need a logo design and stationary set including letterhead, business card (double sided), compliments slip and envelope for a new company Bright Lantern Media.
The files should be editable to update address and standard contact details, will need to forward to web designer and stationary printer.
The company will be an online marketer and distributer of various business education products in Australia.
The designs should convey simple clean image
Target Market(s)
Small business owners and professional service providers (ie Accountants, Lawyers, Real Estate Agents) in Australia
Industry/Entity Type
Education
Look and feel
Each slider illustrates characteristics of the customer's brand and the style your logo design should communicate.

```html
<!DOCTYPE html>
<html lang="en">
<head>
<meta charset="utf-8">
<title>Bright Lantern Media – Business Card</title>
<link rel="stylesheet" href="https://fonts.googleapis.com/css2?family=Arimo:wght@400;700&display=swap">
<style>
  :root {
    --page: #ffffff;
    --card: #4b5660;
    --ink: #ffffff;
    --accent: #1a9be0;
  }
  * { box-sizing: border-box; margin: 0; padding: 0; }
  html, body {
    width: 1200px;
    height: 363px;
    overflow: hidden;
    background: var(--page);
    font-family: "Arimo", Arial, sans-serif;
  }
  .sheet {
    position: relative;
    width: 1200px;
    height: 363px;
  }
  .card {
    position: absolute;
    top: 76px;
    width: 460px;
    height: 216px;
    border-radius: 18px;
    background: var(--card);
    color: var(--ink);
  }
  .card--front { left: 75px; }
  .card--back { left: 662px; }

  .brand {
    position: absolute;
    display: flex;
    align-items: center;
    gap: 8px;
    font-weight: 400;
    color: var(--ink);
    white-space: nowrap;
    letter-spacing: -0.5px;
  }
  .brand__mark {
    display: block;
    background: var(--accent);
  }
  .card--front .brand {
    right: 34px;
    bottom: 30px;
    font-size: 29px;
  }
  .card--front .brand__mark { width: 14px; height: 14px; }
  .card--back .brand {
    left: 20px;
    top: 28px;
    font-size: 25px;
  }
  .card--back .brand__mark { width: 12px; height: 12px; }

  .contact {
    position: absolute;
    left: 262px;
    top: 120px;
    padding: 2px 0 2px 20px;
    font-size: 12px;
    line-height: 15px;
  }
  .contact__bracket {
    position: absolute;
    left: 0;
    top: 0;
    width: 8px;
    height: 100%;
    border: 3px solid var(--accent);
    border-right: none;
  }
  .contact__name { font-weight: 700; }
</style>
</head>
<body>
  <main class="sheet">
    <section class="card card--front" aria-label="Business card front">
      <div class="brand">
        <span class="brand__mark" aria-hidden="true"></span>
        <span class="brand__name">Bright Lantern Media</span>
      </div>
    </section>

    <section class="card card--back" aria-label="Business card back">
      <div class="brand">
        <span class="brand__mark" aria-hidden="true"></span>
        <span class="brand__name">Bright Lantern Media</span>
      </div>
      <address class="contact" style="font-style: normal;">
        <span class="contact__bracket" aria-hidden="true"></span>
        <div class="contact__name">Daniel Harlow</div>
        <div>2187 Ridgeway Crescent</div>
        <div>612.490.3718</div>
        <div>info@brightlantern.com.au</div>
        <div>www.brightlantern.com.au</div>
      </address>
    </section>
  </main>
</body>
</html>
```